Eye-catching & Glamorous Labels for Skincare Bottles & Jars

We need new labels designed for our product range as we have been dormant for a few years and are now rebranding Velora Grace - Kindly Made Skincare. The label sizes are defined in the attached word document. All products have either a bright silver or a matte silver lid pump/spray so please keep this in mind.

We are open to colours and invite you to create bright trendy labels which are coordinated with the logo attached. The logo is not of any specific colour so dark on light, light on dark, tone on tone - we like purple / duck egg blue / turquoise WITH matte silver, however stronger colours like navy plus maroon with matte silver is also a strong favourite. If you feel inspired by a colour you think would be appropriate to Velora Grace please feel free to have a go.

A front section for product information is required and the back should include relevant details ie ingredients, company info, and a note that there has been no testing on animals.

The serum bottle will require a front and back label on a clear label in a pale colour to coordinate with the rest of the range. Size for this label is 35mm top edge, 25mm bottom edge, height 45mm - I have attached a picture of the serum bottle as they were originally pad printed. Please don't hesitate to contact me for any further information. Good luck!

Target Market(s)

Educated professional women 30-45 who are regular skincare users and looking for beautiful skincare products without animal derived ingredients and animal testing

Industry/Entity Type

Skin Care Product

Font styles to use
Serif
Sans Serif
Decorative
Script

Colors

Designer to choose colors to be used in the design.

Requirements
Must have
• Velora Grace Logo - eye catching design - not too busy or cramped.
Nice to have
• Is it possible to create a background pattern using a very small image of the logo? Just a thought.

```html
<!DOCTYPE html>
<html lang="en">
<head>
<meta charset="utf-8">
<title>Velora Grace – Satin Renewal Day Cream Label</title>
<link rel="stylesheet" href="https://fonts.googleapis.com/css2?family=Cinzel:wght@400;500&family=Raleway:wght@300;400&family=Open+Sans:wght@400;600;700&display=swap">
<style>
  :root {
    --page: #ffffff;
    --band-top: #f3f3f3;
    --band-bottom: #e4e4e4;
    --brand-grey: #9b9593;
    --gold: #e2b03f;
    --gold-soft: #f1d79a;
    --ink: #6f6f6f;
    --ink-dark: #555555;
    --pattern-grey: #c9c6c4;
  }
  * { margin: 0; padding: 0; box-sizing: border-box; }
  html, body { width: 1158px; height: 1200px; overflow: hidden; background: var(--page); }
  .canvas { position: relative; width: 1158px; height: 1200px; }

  .label-band {
    position: absolute; left: 32px; top: 336px; width: 1094px; height: 767px;
    background: linear-gradient(180deg, var(--band-top) 0%, var(--band-bottom) 100%);
  }

  .front-panel {
    position: absolute; left: 289px; top: 0; width: 500px; height: 651px;
    text-align: center;
  }
  .brand-name {
    position: absolute; top: 140px; left: 0; width: 100%;
    font-family: "Cinzel", serif; font-weight: 500; font-size: 58px;
    color: var(--brand-grey); letter-spacing: 2px; line-height: 62px;
  }
  .product-name {
    position: absolute; top: 354px; left: 0; width: 100%;
    font-family: "Cinzel", serif; font-weight: 500; font-size: 50px;
    color: var(--gold); line-height: 50px; letter-spacing: 1px;
  }
  .product-type {
    position: absolute; top: 462px; left: 0; width: 100%;
    font-family: "Raleway", sans-serif; font-weight: 300; font-size: 27px;
    color: var(--brand-grey); letter-spacing: 2px; line-height: 32px;
  }
  .front-ornament {
    position: absolute; top: 538px; left: 237px; width: 26px; height: 26px;
    background: radial-gradient(circle, var(--gold) 0%, var(--gold-soft) 70%, transparent 72%);
  }

  .back-panel {
    position: absolute; left: 778px; top: 34px; width: 244px;
    font-family: "Open Sans", sans-serif; color: var(--ink);
  }
  .ingredients-title { font-size: 13px; font-weight: 600; letter-spacing: .5px; color: var(--ink-dark); line-height: 18px; }
  .ingredients-list { font-size: 12px; line-height: 18.4px; text-align: justify; }

  .cruelty-free {
    margin-top: 22px; display: flex; align-items: center; justify-content: space-between;
    width: 244px; height: 54px; border: 2px solid var(--ink); border-radius: 27px;
    padding: 0 6px 0 16px;
  }
  .cruelty-free-text { font-size: 11.5px; font-weight: 700; line-height: 14px; color: var(--ink-dark); text-align: center; }
  .cruelty-free-seal { width: 40px; height: 40px; border-radius: 50%; background: var(--ink); flex: none; }

  .company-address { margin-top: 24px; font-size: 12.5px; line-height: 17px; }
  .net-volume { margin-top: 22px; font-size: 12.5px; font-weight: 600; color: var(--ink-dark); }
  .origin { margin-top: 10px; font-size: 12.5px; font-weight: 600; color: var(--ink-dark); }

  .pattern-strip {
    position: absolute; left: 0; top: 651px; width: 1094px; height: 116px;
    background: linear-gradient(90deg, var(--pattern-grey) 0%, var(--gold-soft) 50%, var(--pattern-grey) 100%);
    opacity: .75;
  }
</style>
</head>
<body>
<main class="canvas">
  <section class="label-band">
    <div class="front-panel">
      <div class="brand-name">Velora<br>Grace</div>
      <h1 class="product-name">SATIN<br>RENEWAL</h1>
      <div class="product-type">DAY CREAM</div>
      <div class="front-ornament" role="img" aria-label="Small gold four-petal ornament"></div>
    </div>

    <div class="back-panel">
      <div class="ingredients-title">INGREDIENT</div>
      <p class="ingredients-list">Aqua, Glycerin, Caprylic Triglyceride, Cetearyl Alcohol, Shea Butter, Squalane, Niacinamide, Sodium Hyaluronate, Palmitoyl Tripeptide, Rosehip Seed Oil, Jojoba Seed Oil, Aloe Leaf Juice, Green Tea Extract, Chamomile Extract, Panthenol, Tocopherol, Allantoin, Ceramide NP, Cetyl Alcohol, Glyceryl Stearate, Xanthan Gum, Sodium Benzoate, Potassium Sorbate, Citric Acid, Lavender Oil, Sweet Almond Oil, Argan Kernel Oil, Vitamin C, Bisabolol, Rice Bran Extract, Oat Kernel Flour, Pea Peptide, Licorice Root Extract, Centella Extract, Lactic Acid, Cucumber Extract, Marula Oil, Parfum.</p>

      <div class="cruelty-free">
        <span class="cruelty-free-text">WE GUARANTEE OUR<br>PRODUCTS WITHOUT<br>TESTING ON ANIMALS</span>
        <span class="cruelty-free-seal" role="img" aria-label="Cruelty-free certification seal"></span>
      </div>

      <p class="company-address">1820 Meadowlark Lane,<br>Brookfield, OR 97008</p>
      <p class="net-volume">100ml (3.3US FL OZ)</p>
      <p class="origin">MADE IN USA</p>
    </div>

    <div class="pattern-strip" role="img" aria-label="Decorative band of grey and gold geometric petal pattern"></div>
  </section>
</main>
</body>
</html>
```